brix4lane

i want to ues this logo and the same colors used on the business card

cleaning & service

Industry/Entity Type

Business

Contact Information for Business Card

Font styles to use
Serif
Sans Serif
Decorative
Script

Colors
add136
0692cd
000000
5c5c5c
fbfbfb

Requirements
Must have
• cleaning things

```html
<!DOCTYPE html>
<html lang="en">
<head>
<meta charset="utf-8">
<title>brix4lane business card</title>
<link href="https://fonts.googleapis.com/css2?family=Work+Sans:wght@400;500;600&display=swap" rel="stylesheet">
<style>
  :root {
    --brand-green: #a6ce3e;
    --brand-blue: #0a6fb8;
    --line-blue: #4a9ad6;
    --text-grey: #3d3d3d;
    --card-white: #ffffff;
    --page-bg: #2b2b2b;
  }
  * { margin: 0; padding: 0; box-sizing: border-box; }
  html, body {
    width: 1200px; height: 930px; overflow: hidden;
    background: var(--page-bg);
    font-family: "Work Sans", Arial, sans-serif;
  }
  .card {
    position: absolute;
    left: 278px;
    width: 644px; height: 368px;
    border-radius: 24px;
    overflow: hidden;
  }
  .card-front { top: 76px; background: var(--card-white); }
  .card-back { top: 486px; background: var(--brand-green); }

  .brand-mark {
    position: absolute; left: 34px; top: 112px;
    display: flex; align-items: center; gap: 8px;
    font-weight: 600; font-size: 28px; color: var(--brand-blue);
  }
  .brand-mark .dot {
    width: 14px; height: 14px; border-radius: 50%; background: var(--brand-green);
  }
  .holder {
    position: absolute; right: 28px; top: 186px; text-align: right;
  }
  .holder-name {
    font-weight: 500; font-size: 26px; letter-spacing: 1.5px;
    color: var(--brand-blue); line-height: 1;
  }
  .holder-role {
    font-size: 16px; color: var(--text-grey); margin-top: 6px;
  }
  .divider {
    position: absolute; left: 34px; right: 27px; top: 248px;
    height: 1.5px; background: var(--line-blue);
  }
  .address {
    position: absolute; left: 34px; top: 282px;
    font-size: 16px; line-height: 20px; color: var(--text-grey);
  }
  .contacts {
    position: absolute; right: 26px; top: 262px;
    list-style: none; font-size: 16px; line-height: 20px; color: var(--text-grey);
  }
  .contacts li { display: flex; align-items: center; justify-content: flex-end; gap: 12px; }
  .contacts svg { width: 12px; height: 12px; }
  .edge-band { position: absolute; left: 0; bottom: 0; width: 644px; height: 34px; }

  .back-mark {
    position: absolute; inset: 0;
    display: flex; align-items: center; justify-content: center; gap: 14px;
    font-weight: 600; font-size: 46px; color: var(--card-white);
  }
  .back-mark .dot {
    width: 22px; height: 22px; border-radius: 50%; background: var(--card-white);
  }
</style>
</head>
<body>
  <section class="card card-front">
    <div class="brand-mark"><span class="dot"></span>brix4lane</div>

    <div class="holder">
      <div class="holder-name">MARLA QUINN</div>
      <div class="holder-role">Director</div>
    </div>

    <div class="divider"></div>

    <p class="address">47 Alder Grove Rd,<br>Toronto ON M4K 2P9</p>

    <ul class="contacts">
      <li>+330 2814-5903
        <svg viewBox="0 0 12 12"><path d="M3 1 L5 3.5 L4 5 Q5 7.5 7 8 L8.5 7 L11 9 L9.5 11 Q4 10.5 1 3 Z" fill="var(--brand-blue)"/></svg>
      </li>
      <li>info@brix4lane.com
        <svg viewBox="0 0 12 12"><rect x="1" y="2.5" width="10" height="7" fill="none" stroke="var(--brand-blue)" stroke-width="1.4"/><path d="M1 3 L6 7 L11 3" fill="none" stroke="var(--brand-blue)" stroke-width="1.2"/></svg>
      </li>
      <li>www.brix4lane.com
        <svg viewBox="0 0 12 12"><g fill="none" stroke="var(--brand-blue)" stroke-width="1"><circle cx="6" cy="6" r="5"/><ellipse cx="6" cy="6" rx="2.2" ry="5"/><path d="M1 6 H11 M2 3.5 H10 M2 8.5 H10"/></g></svg>
      </li>
    </ul>

    <svg class="edge-band" viewBox="0 0 644 34" preserveAspectRatio="none">
      <path d="M0 12 H360 Q372 12 366 16 H0 Z" fill="var(--brand-green)"/>
      <path d="M0 16 H370 Q380 16 386 14 L400 7 Q412 1 430 1 H644 V34 H0 Z" fill="var(--card-white)"/>
      <path d="M0 19 H372 Q384 19 392 15 L404 9 Q416 3 432 3 H644 V34 H0 Z" fill="var(--brand-blue)"/>
    </svg>
  </section>

  <section class="card card-back">
    <div class="back-mark"><span class="dot"></span>brix4lane</div>
  </section>
</body>
</html>
```